Orbit 528 - Pagevo Book Cover

I am looking for a Pagevo book cover for my book about "Orbit 528".
The Book is Titled:
Orbit 528 Advanced
Shaping Tomorrow: Paths Toward Unlocking Hidden Cosmic Laws
Author is Dorian Welby
Here is a book description that may help you understand more about it:
Inspired by the genius of Anton Brevik, this comprehensive guide delves into the ancient wisdom and cutting-edge science behind the 369 method, a powerful tool for manifesting your desires. Whether you're seeking personal growth, financial success, or spiritual enlightenment, this book provides advanced techniques and methods to transform your dreams into reality.
Any questions please ask.
Thanks
Colin

```html
<!DOCTYPE html>
<html lang="en">
<head>
<meta charset="utf-8">
<title>Orbit 528 Advanced — Dorian Welby</title>
<link rel="stylesheet" href="https://fonts.googleapis.com/css2?family=Anton&family=Didact+Gothic&family=Tinos:wght@400;700&display=swap">
<style>
  :root {
    --bg-light: #eeeeee;
    --bg-mid: #d2d2d2;
    --bg-dark: #b3b3b3;
    --ink-navy: #262747;
    --ink-indigo: #3b3d78;
    --ink-black: #111111;
    --art-light: #f1f1f1;
    --art-mid: #c9c9c9;
    --art-dark: #8d8d8d;
  }
  * { margin: 0; padding: 0; box-sizing: border-box; }
  html, body {
    width: 805px;
    height: 1200px;
    overflow: hidden;
    background: var(--bg-mid);
  }
  .cover {
    position: relative;
    width: 805px;
    height: 1200px;
    overflow: hidden;
    background:
      radial-gradient(ellipse 70% 45% at 50% 0%, var(--bg-light) 0%, rgba(238,238,238,0) 100%),
      linear-gradient(180deg, var(--bg-mid) 0%, #c6c6c6 55%, var(--bg-dark) 100%);
  }
  .series-title {
    position: absolute;
    top: 92px;
    left: 0;
    width: 100%;
    text-align: center;
    font-family: "Anton", sans-serif;
    font-size: 172px;
    line-height: 1;
    letter-spacing: 4px;
    color: var(--ink-navy);
  }
  .emblem {
    position: absolute;
    left: 83px;
    top: 228px;
    width: 640px;
    height: 620px;
  }
  .emblem-number {
    position: absolute;
    top: 476px;
    left: 0;
    width: 100%;
    text-align: center;
    font-family: "Didact Gothic", sans-serif;
    font-size: 104px;
    line-height: 1;
    color: var(--ink-black);
  }
  .edition {
    position: absolute;
    top: 800px;
    left: 107px;
    width: 640px;
    font-family: "Anton", sans-serif;
    font-size: 58px;
    line-height: 1;
    color: var(--ink-navy);
    display: flex;
    justify-content: space-between;
  }
  .subtitle {
    position: absolute;
    top: 903px;
    left: 0;
    width: 100%;
    text-align: center;
    font-family: "Tinos", serif;
    color: var(--ink-indigo);
  }
  .subtitle-lead {
    display: block;
    font-weight: 700;
    font-size: 27px;
    line-height: 34px;
  }
  .subtitle-line {
    display: block;
    font-weight: 400;
    font-size: 26px;
    line-height: 32px;
  }
  .author {
    position: absolute;
    top: 1106px;
    left: 0;
    width: 100%;
    text-align: center;
    font-family: "Tinos", serif;
    font-size: 54px;
    line-height: 1;
    letter-spacing: 22px;
    padding-left: 22px;
    color: var(--ink-black);
  }
</style>
</head>
<body>
  <main class="cover">
    <h1 class="series-title">ORBIT</h1>

    <svg class="emblem" viewBox="0 0 640 620" role="img" aria-label="Sacred-geometry mandala illustration: concentric circles, interlocking petals and radiating spokes in fine black linework">
      <defs>
        <radialGradient id="emblem-fill" cx="50%" cy="50%" r="50%">
          <stop offset="0%" stop-color="var(--art-light)"/>
          <stop offset="55%" stop-color="var(--art-mid)"/>
          <stop offset="100%" stop-color="var(--art-dark)" stop-opacity="0.55"/>
        </radialGradient>
      </defs>
      <circle cx="320" cy="306" r="290" fill="url(#emblem-fill)"/>
    </svg>

    <div class="emblem-number">528</div>

    <p class="edition" aria-label="Advanced">
      <span>A</span><span>D</span><span>V</span><span>A</span><span>N</span><span>C</span><span>E</span><span>D</span>
    </p>

    <h2 class="subtitle">
      <span class="subtitle-lead">SHAPING TOMORROW:</span>
      <span class="subtitle-line">Paths Toward Unlocking</span>
      <span class="subtitle-line">Hidden Cosmic Laws</span>
    </h2>

    <p class="author">DORIAN WELBY</p>
  </main>
</body>
</html>
```